Web Design Project for new Anaesthetic Pracitice

We have recently obtained our brand new logo from PixelHarbor and now it's time to move on to our website. We are a new anaesthetic practice that offers state of the art anaesthesia care.

We are after a design that communicates professionalism, along with a modern, forward thinking attitude.

Reason: I would like the chance to see more designs. I have also increased the budget and will be providing a little more guidance on required elements.

I have just increased the budget on this project.  $400 for first place, $100 for second.

Also view the brief for some further guidance to help refine designs

Reason: As our deadline is now almost upon us and we have only just sorted out the issues with our increased budget I thought it only fair to give other designers a chance to see if they wish to participate. As a consolation to you all the project is now guaranteed.

Target Market(s)

Our patients and to a lesser extent the surgeons we work with

Requirements
Must have
• The same clean, sleek modern look that we have in our logo. The logo should feature prominently (examples are uploaded)

Menu system, either vertical or horizontal.
The menu system will include the following:
• Home
• Our People
• Our Hospitals
• Our Charges
• Booking Form
• Patient Information
• Contact Information

If designers think they can find more succinct wording for these categories they are free to try.

Some of these menu entries will in all probability lead to a drop down menu (Or People, Our Hospitals and Patient Information in particular). Consideration to how these menus will look and what they are likely to cover is a must.

If your design is selected you will be asked to produce a PSD for both the main page and for any secondary pages (which will be a development of the main page, with the same basic layout, just with a single lot of content) unless your design is one where all pages on the site look the same (i.e. the main page does not have portions of the other pages or leaders on it)

Design delivered as a layered PSD file so we can have our coders chop and slice it into a CSS website.

Use of the logo as uploaded below

A space reserved for breadcrumbs.

Use of the TrustVane logo, preferably in the footer, but we will accept it at the bottom of a side bar. Examples are included below.

The font in the logo is Sommet. We have the ability to install this as a webfont, feel free to utilise it in the site if you so wish.

Contact information can be either a menu option or in the footer.

Nice to have
• Rotating images (either provide us with dummies or just blank placeholder spaces, we have an in-house professional photographer who will be able to populate any such area)

Either a design with all pages on the site looking the same or with a main home page and a separate, related design for other pages (the full site will have about 30 pages, covering how to get to the office, how to get to the hospitals we work at (with roamly charts), the doctors working for us, our office staff, some information on why we charge what we do, and a range of patient information pages)

Icons for Chatterly and Blipster. We have no need for Vid Nest, Pokk, Snapro or Murmo right now, but if you want to include icons for these, feel free, we can always use them later.

These sort of icons can be placed anywhere but personally I like them in the footer.

A footer menu is not mandatory but if it works better with your design feel free to do so.
Should not have
• Pictures of young doctors in white coats, stethoscopes, cadeucus (staff and serpent), all are clichéd and worn out.

```html
<!DOCTYPE html>
<html lang="en">
<head>
<meta charset="utf-8">
<title>Our People – Loddon Ridge Anaesthetic Specialists</title>
<link href="https://fonts.googleapis.com/css2?family=Exo+2:wght@500;600;700&family=Arimo:wght@400&display=swap" rel="stylesheet">
<style>
:root{
  --red:#e21f26;
  --ink:#333;
  --ink-soft:#3d3d3d;
  --brand-ink:#4a4a4a;
  --nav-top:#2a2a2a;
  --nav-bottom:#050505;
  --nav-divider:#333;
  --footer-top:#3a3a3a;
  --footer-bottom:#000;
  --page:#f3f3f3;
  --white:#fff;
}
*{margin:0;padding:0;box-sizing:border-box}
html,body{width:1200px;height:963px;overflow:hidden}
body{
  position:relative;
  background:radial-gradient(ellipse 620px 420px at 600px 520px,#fff 0%,#fafafa 55%,var(--page) 100%);
  font-family:"Arimo",Arial,sans-serif;color:var(--ink);
}
.top-rule{position:absolute;left:0;top:0;width:1200px;height:5px;background:var(--red)}

.brand{position:absolute;left:310px;top:36px;display:flex;align-items:center;gap:10px}
.brand-square{width:12px;height:12px;background:var(--red);flex:none}
.brand-name{font-family:"Exo 2",sans-serif;font-weight:600;font-size:23px;line-height:26px;color:var(--brand-ink);white-space:nowrap}

.assist{position:absolute;left:720px;top:29px;font-family:"Exo 2",sans-serif;font-weight:600;font-size:17px;color:#3a3a3a;white-space:nowrap}
.assist .call{color:var(--red);margin-left:10px}
.assist .num{font-weight:500}
.search{position:absolute;left:859px;top:66px;width:169px;height:25px;display:flex;border:1px solid #d4d4d4;background:var(--white)}
.search span{flex:1;font-size:10px;color:#999;padding:6px 5px}
.search button{width:28px;border:0;background:linear-gradient(#d8d8d8,#b9b9b9);display:flex;align-items:center;justify-content:center}

.main-nav{position:absolute;left:159px;top:132px;width:883px;height:53px;background:linear-gradient(var(--nav-top),var(--nav-bottom));border:1px solid #000;display:flex}
.main-nav a{font-family:"Exo 2",sans-serif;font-weight:600;font-size:13.5px;color:var(--white);text-decoration:none;display:flex;align-items:center;justify-content:center;white-space:nowrap;border-right:1px solid var(--nav-divider);flex:none}
.main-nav a:last-child{border-right:0;flex:1}
.main-nav a.active{background:var(--red)}
.nav-home{width:66px}
.nav-people{width:99px}
.nav-hospitals{width:121px}
.nav-charges{width:111px}
.nav-booking{width:117px}
.nav-patient{width:168px}
.nav-contact{width:77px}

.banner{position:absolute;left:159px;top:190px;width:883px;height:149px;background:linear-gradient(#fff,#e6e6e6)}
.banner h1{position:absolute;left:0;width:400px;top:42px;text-align:center;font-family:"Exo 2",sans-serif;font-weight:600;font-size:28px;line-height:36px;color:var(--red)}
.banner-photo{position:absolute;right:0;top:0;width:424px;height:149px;background:linear-gradient(90deg,rgba(230,238,242,0) 0%,#bcd9e6 25%,#8fc3db 60%,#cfe2ea 100%)}

.breadcrumb{position:absolute;left:161px;top:352px;font-size:11px;color:#222}
.breadcrumb .sep{font-size:8px;margin:0 3px;color:#666}
.breadcrumb .current{color:var(--red)}
.page-title{position:absolute;left:161px;top:398px;font-family:"Exo 2",sans-serif;font-weight:600;font-size:28px;color:var(--red)}

.copy{position:absolute;font-size:10.6px;line-height:17.5px;color:var(--ink-soft)}
.copy p+p{margin-top:17.5px}
.copy-narrow{left:167px;top:449px;width:480px}
.copy-wide{left:167px;top:664px;width:855px}
.portrait{position:absolute;left:690px;top:409px;width:330px;height:218px;border-radius:8px;border:3px solid #c9c9c9;background:radial-gradient(ellipse at 55% 40%,#4a7fb6 0%,#2d5a93 45%,#1f3550 100%)}

.site-footer{position:absolute;left:0;top:842px;width:1200px;height:121px;background:linear-gradient(var(--footer-top),#111 45%,var(--footer-bottom))}
.trust-badge{position:absolute;left:159px;top:24px;width:101px;height:58px;border-radius:4px;background:var(--white);border-bottom:10px solid var(--red)}
.copyright{position:absolute;left:281px;top:46px;font-size:11px;color:#eee;white-space:nowrap}
.social{position:absolute;left:640px;top:45px;display:flex;gap:16px}
.social a{display:flex;align-items:center;gap:6px;font-size:11px;color:#ddd;text-decoration:none;white-space:nowrap}
.social i{width:14px;height:14px;border-radius:50%;background:#8a8a8a;display:block}
.footer-brand{position:absolute;left:856px;top:31px;display:flex;align-items:center;gap:8px}
.footer-brand .brand-name{color:var(--white);font-size:17px;line-height:20px}
</style>
</head>
<body>
<div class="top-rule"></div>

<header>
  <div class="brand">
    <span class="brand-square"></span>
    <span class="brand-name">Loddon Ridge<br>Anaesthetic Specialists</span>
  </div>
  <div class="assist">NEED ASISTANCE? <span class="call">CALL-</span><span class="num">(123)555-0148</span></div>
  <div class="search">
    <span>Search...</span>
    <button aria-label="Search">
      <svg width="12" height="12" viewBox="0 0 12 12"><circle cx="5" cy="5" r="3.3" fill="none" stroke="#fff" stroke-width="1.6"/><line x1="7.5" y1="7.5" x2="11" y2="11" stroke="#fff" stroke-width="2"/></svg>
    </button>
  </div>
</header>

<nav class="main-nav">
  <a href="#" class="nav-home">HOME</a>
  <a href="#" class="nav-people active">OUR PEOPLE</a>
  <a href="#" class="nav-hospitals">OUR HOSPITALS</a>
  <a href="#" class="nav-charges">OUR CHARGES</a>
  <a href="#" class="nav-booking">BOOKING FORM</a>
  <a href="#" class="nav-patient">PATIENT INFORMATION</a>
  <a href="#" class="nav-contact">CONTACT</a>
  <a href="#" class="nav-info">INFORMATION</a>
</nav>

<section class="banner">
  <h1>ABOUT LRAS Research<br>and development</h1>
  <div class="banner-photo" role="img" aria-label="Surgical team in blue scrubs working in an operating theatre"></div>
</section>

<div class="breadcrumb">Home <span class="sep">&#187;</span> <span class="current">Our people</span></div>

<h2 class="page-title">Our People</h2>

<div class="copy copy-narrow">
  <p>Loddon Ridge Anaesthetic Specialists (LRAS), is a global leader in the design, manufacture and service of veterinary anesthesia equipment and critical care products. RVA is owned by veterinarians who specialize in anesthesia and engineer equipment that is easy for anesthesia specialists and the general practitioner to use. The number one priority of our company is to solve the anesthetic challenges for veterinarians and ensure patient safety.</p>
  <p>We focus our research on developing innovative anesthesia equipment that helps save the veterinarian money by lowering anesthetic gas costs. We also improve the environment by reducing the waste gas pollutants produced during anesthetic procedures. We have now expanded operations to include North America bringing these new advances in anesthesia to the United States and Canada.</p>
</div>

<div class="portrait" role="img" aria-label="Anaesthetist in cap and mask holding an anaesthesia mask"></div>

<div class="copy copy-wide">
  <p>Loddon Ridge Anaesthetic Specialists (LRAS), is a global leader in the design, manufacture and service of veterinary anesthesia equipment and critical care products. RVA is owned by veterinarians who specialize in anesthesia and engineer equipment that is easy for anesthesia specialists and the general practitioner to use. The number one priority of our company is to solve the anesthetic challenges for veterinarians and ensure patient safety.</p>
  <p>We focus our research on developing innovative anesthesia equipment that helps save the veterinarian money by lowering anesthetic gas costs. We also improve the environment by reducing the waste gas pollutants produced during anesthetic procedures. We have now expanded operations to include North America bringing these new advances in anesthesia to the United States and Canada.</p>
</div>

<footer class="site-footer">
  <div class="trust-badge" role="img" aria-label="TrustVane security badge"></div>
  <p class="copyright">Copyright @ 2013 www.lodridgecare.com. All rights reserved.</p>
  <div class="social">
    <a href="#"><i></i>Blipster</a>
    <a href="#"><i></i>Chatterly</a>
  </div>
  <div class="footer-brand">
    <span class="brand-square"></span>
    <span class="brand-name">Loddon Ridge<br>Anaesthetic Specialists</span>
  </div>
</footer>
</body>
</html>
```